Business Cards for new orthopaedic surgery practice

My husband and I are starting our own orthopaedic surgery practice. We are looking for a business card that is uniform, but one will have my name/title and the other will have his. You can just create one design with my name on it for now. But when I choose your design as the winning design I will ask that you add another copy with his name/title.

We are looking for classy, simple, elite all in one. We like dark blues/a little gold/yellow. Something that goes with our logo. We want our logo incorporated. Here is all the info you need:
Business name: RV Spine & Vitality Center
Location: 38157 North Harbor Blvd
Palm Hollow, GA 33058
Phone: 954-218-4630
Fax: 954-581-2473
Email: info@myrvspine.example

Names: Lorena Vickers, M.D.
Board Certified Hand and Upper Extremity Surgeon

Eban Sorley, M.D.
Board Certified Hip & Knee Replacement/General Orthopaedic Surgeon

Can decide what you want to put on the back. Maybe a slogan:
Rooted in Care. Focused on You

I am just going to upload our logo. The only thing is if we select you as the winning design, the location, and phone numbers may change. We will need your help to update that once fully solidified.

Industry/Entity Type

Medical

Contact Information for Business Card

Colors
0054AA
0677BA
7BADD7
CADEEF
E8F1F8
0094D4
00A9DD
6FCCEA
C7EBF8
E9F6FB

Requirements
Must have
• class, appeal,
Should not have
• We want to air on the side of masculine if we are looking at masculine vs. feminine feel. But we still want it classy, sophisticated, and something we will love

```html
<!DOCTYPE html>
<html lang="en">
<head>
<meta charset="utf-8">
<title>RV Spine &amp; Vitality Center – Business Card</title>
<link href="https://fonts.googleapis.com/css2?family=Poppins:wght@500;600&family=Arimo:wght@400;600&display=swap" rel="stylesheet">
<style>
  :root {
    --backdrop: #e4d7cb;
    --navy: #36456a;
    --gold: #ebc92b;
    --display: "Poppins", sans-serif;
    --body: "Arimo", sans-serif;
  }
  * { box-sizing: border-box; margin: 0; padding: 0; }
  html, body { width: 1200px; height: 894px; overflow: hidden; }
  body { background: var(--backdrop); position: relative; }

  .card {
    position: absolute;
    left: 320px;
    width: 552px;
    height: 315px;
    overflow: hidden;
  }
  .card--front { top: 110px; background: var(--navy); }
  .card--back  { top: 483px; background: var(--gold); }

  .joint-art { position: absolute; top: 0; height: 100%; width: 150px; }
  .joint-art--left  { left: 0; }
  .joint-art--right { right: 0; }
  .card--front .joint-art { background: var(--gold); }
  .card--back .joint-art  { background: var(--navy); }

  .wordmark {
    position: absolute;
    left: 50%;
    transform: translateX(-50%);
    border-radius: 50%;
    border: 1.5px solid currentColor;
    display: flex;
    align-items: center;
    justify-content: center;
    text-align: center;
    font-family: var(--display);
    font-weight: 600;
    line-height: 1.2;
  }
  .card--front .wordmark {
    top: 90px; width: 140px; height: 140px;
    color: var(--gold); font-size: 17px;
  }
  .card--back .wordmark {
    top: 62px; width: 100px; height: 100px;
    color: var(--navy); font-size: 12px;
  }

  .practice-name {
    position: absolute;
    top: 266px; left: 0; width: 100%;
    text-align: center;
    font-family: var(--display);
    font-weight: 600;
    font-size: 17px;
    color: var(--gold);
  }

  .slogan {
    position: absolute;
    top: 16px; left: 0; width: 100%;
    text-align: center;
    font-family: var(--body);
    font-weight: 600;
    font-size: 15px;
    color: var(--navy);
  }

  .person {
    position: absolute;
    top: 180px; left: 160px;
    display: flex; align-items: center; gap: 10px;
    color: var(--navy);
  }
  .person__icon {
    width: 34px; height: 34px;
    border: 1.5px solid var(--navy);
    border-radius: 50%;
    display: flex; align-items: center; justify-content: center;
  }
  .person__name { font-family: var(--body); font-weight: 600; font-size: 18px; line-height: 1.1; }
  .person__title { font-family: var(--body); font-weight: 600; font-size: 5.5px; margin-top: 2px; }

  .contacts {
    position: absolute;
    top: 229px; left: 170px;
    display: grid;
    grid-template-columns: 102px 150px;
    row-gap: 8px;
    font-family: var(--body);
    font-size: 7.5px;
    color: var(--navy);
  }
  .contact { display: flex; align-items: center; gap: 8px; line-height: 1.3; }
  .contact__icon {
    width: 14px; height: 14px; flex: none;
    border: 1px solid var(--navy);
    border-radius: 50%;
    display: flex; align-items: center; justify-content: center;
  }
</style>
</head>
<body>

<section class="card card--front" aria-label="Business card front">
  <div class="joint-art joint-art--left" role="img" aria-label="Stylized joint bone illustration"></div>
  <div class="joint-art joint-art--right" role="img" aria-label="Stylized joint bone illustration"></div>
  <div class="wordmark">RV Spine &amp;<br>Vitality Center</div>
  <p class="practice-name">RV Spine &amp; Vitality Center</p>
</section>

<section class="card card--back" aria-label="Business card back">
  <div class="joint-art joint-art--left" role="img" aria-label="Stylized joint bone illustration"></div>
  <div class="joint-art joint-art--right" role="img" aria-label="Stylized joint bone illustration"></div>
  <p class="slogan">Steady in Care, Centered on You</p>
  <div class="wordmark">RV Spine &amp;<br>Vitality Center</div>

  <div class="person">
    <div class="person__icon">
      <svg width="18" height="18" viewBox="0 0 18 18" fill="#36456a"><circle cx="9" cy="6" r="3.5"/><path d="M2.5 16c0-3.6 2.9-5.5 6.5-5.5s6.5 1.9 6.5 5.5z"/></svg>
    </div>
    <div>
      <p class="person__name">Lorena Vickers, M.D.</p>
      <p class="person__title">Board Certified Hand and Upper Extremity Surgeon</p>
    </div>
  </div>

  <div class="contacts">
    <div class="contact">
      <span class="contact__icon"><svg width="8" height="8" viewBox="0 0 10 10" fill="#36456a"><path d="M2 0.5l2 2.2-1 1.2c.7 1.4 1.7 2.4 3.1 3.1l1.2-1 2.2 2-1.2 1.6C4.5 9.3.7 5.5.5 1.7z"/></svg></span>
      <span>954-218-4630</span>
    </div>
    <div class="contact">
      <span class="contact__icon"><svg width="8" height="8" viewBox="0 0 10 10" fill="#36456a"><path d="M1 2h8v6H1zM2 3.2v.2l3 2 3-2v-.2z" fill-rule="evenodd"/></svg></span>
      <span>info@myrvspine.example</span>
    </div>
    <div class="contact">
      <span class="contact__icon"><svg width="8" height="8" viewBox="0 0 10 10" fill="#36456a"><path d="M3 1h4v2H3zM1 3.5h8v4H7.5V9h-5V7.5H1zM3.3 6.3v1.9h3.4V6.3z" fill-rule="evenodd"/></svg></span>
      <span>954-581-2473</span>
    </div>
    <div class="contact">
      <span class="contact__icon"><svg width="8" height="8" viewBox="0 0 10 10" fill="#36456a"><path d="M5 .5a3.3 3.3 0 0 0-3.3 3.3C1.7 6.3 5 9.5 5 9.5s3.3-3.2 3.3-5.7A3.3 3.3 0 0 0 5 .5zm0 2.1a1.2 1.2 0 1 1 0 2.4 1.2 1.2 0 0 1 0-2.4z" fill-rule="evenodd"/></svg></span>
      <span>38157 North Harbor Blvd<br>Palm Hollow, GA 33058</span>
    </div>
  </div>
</section>

</body>
</html>
```